Brochure Cover and Back pages

We are a US-based cosmetics company that sells state-of-the-art skin care products, including advanced anti-aging serums, natural mineral sunscreens, organic antioxidant moisturizers, and organic face cleansers. We need a product brochure. We already have chosen a design for the layout of the product info pages. But we still need a cover page and a back page. We are looking for simple but elegant design for the cover page. The back page is less important and we already know what we want on the back page. It will be the company's mission statement and at the bottom, the company URL, phone number, etc.

The brochure has two folds. So there will be three panels on both sides. The size of each panel is 16.5 (l) x 9.5 (w) cm.

At the end of the project, we expect the designer to integrate all the pages so that the finished copy is read to be sent off to a printing service for printing.

All the product info pages are attached. Also attached are the text (info) to go on the back page, company logo with and without the tagline, the icon in the logo.

YOu are welcome to visit our website www.corvanyx.com to learn about our products.

Industry/Entity Type

Cosmetics

```html
<!DOCTYPE html>
<html lang="en">
<head>
<meta charset="utf-8">
<title>Corvanyx Brochure – Outer Spread</title>
<link rel="stylesheet" href="https://fonts.googleapis.com/css2?family=Open+Sans:wght@400;600;700&family=Oswald:wght@500&family=Comic+Neue:wght@700&display=swap">
<style>
  :root {
    --stage: #d9d9d9;
    --paper: #ffffff;
    --blush: #f7cfd3;
    --blush-soft: #fbe6e8;
    --band-soft: #fdf0f2;
    --rose-text: #e86aa6;
    --rose-dot: #f2b3bd;
    --ink: #1a1a1a;
    --navy: #1f4fa0;
    --band: #e4e4e6;
    --photo-skin: #f1d9cc;
    --photo-warm: #e9c6b3;
    --tube: #e8ecf2;
  }
  * { box-sizing: border-box; margin: 0; padding: 0; }
  html, body { width: 1200px; height: 866px; overflow: hidden; }
  body {
    background: radial-gradient(ellipse at 50% 40%, #eeeeee 0%, var(--stage) 100%);
    font-family: "Open Sans", Arial, sans-serif;
    color: var(--ink);
  }
  .spread {
    position: absolute; left: 30px; top: 103px;
    width: 1140px; height: 660px;
    display: flex;
    box-shadow: 0 12px 30px rgba(0,0,0,.18);
  }
  .panel { position: relative; width: 380px; height: 660px; overflow: hidden; background: var(--paper); }
  .panel + .panel { border-left: 1px solid #eee; }

  /* Product panel */
  .products { padding: 34px 0 0; }
  .products__title { font-family: "Oswald", "Arial Narrow", sans-serif; font-weight: 500; color: var(--navy); font-size: 22px; padding-left: 150px; line-height: 1.1; }
  .products__sub { color: var(--navy); font-size: 12px; padding-left: 150px; margin-bottom: 14px; }
  .product { display: flex; align-items: center; gap: 12px; padding: 22px 24px 22px 40px; height: 170px; }
  .product--shaded { background: var(--band); }
  .product__text { flex: 1; }
  .product__name { font-weight: 700; font-size: 14px; margin-bottom: 6px; }
  .product__desc { font-size: 12px; line-height: 1.4; }
  .product__shot { flex: none; width: 58px; height: 120px; border-radius: 6px 6px 14px 14px; background: linear-gradient(180deg, var(--tube), #ffffff 60%, var(--tube)); }
  .products__contact { position: absolute; bottom: 26px; left: 40px; font-size: 14px; }

  /* Shared */
  .brand { font-family: "Open Sans", Arial, sans-serif; font-weight: 600; color: var(--ink); display: flex; align-items: center; gap: 10px; white-space: nowrap; }
  .brand__dot { width: 12px; height: 12px; border-radius: 50%; background: var(--rose-dot); }
  .soft-band { position: absolute; left: 0; width: 380px; height: 70px; background: linear-gradient(180deg, rgba(255,255,255,0) 0%, var(--band-soft) 50%, rgba(255,255,255,0) 100%); }

  /* Back panel */
  .back { background: linear-gradient(180deg, var(--paper) 0%, var(--paper) 42%, var(--blush-soft) 60%, var(--blush) 100%); }
  .back .brand { position: absolute; top: 150px; left: 0; right: 0; justify-content: center; font-size: 40px; }
  .back .soft-band { top: 255px; }
  .back__copy { position: absolute; top: 360px; left: 0; right: 0; text-align: center; font-family: "Comic Neue", "Comic Sans MS", cursive; font-weight: 700; color: var(--rose-text); }
  .back__mission { font-size: 21px; line-height: 1.35; margin-bottom: 34px; }
  .back__details { font-size: 16px; line-height: 1.4; }
  .back__details p + p { margin-top: 14px; }

  /* Cover panel */
  .cover { background: linear-gradient(180deg, var(--paper) 0%, var(--blush-soft) 30%, var(--paper) 55%, var(--blush-soft) 85%, var(--blush) 100%); }
  .cover .brand { position: absolute; top: 34px; left: 40px; font-size: 34px; }
  .cover__tagline { position: absolute; top: 84px; left: 56px; font-family: "Comic Neue", "Comic Sans MS", cursive; font-weight: 700; font-size: 14px; letter-spacing: .5px; }
  .cover__portrait { position: absolute; top: 130px; left: 60px; right: 0; height: 260px; background: radial-gradient(ellipse at 65% 45%, var(--photo-skin) 0%, var(--photo-warm) 55%, var(--blush-soft) 100%); }
  .cover .soft-band { top: 392px; }
  .cover__products { position: absolute; top: 470px; left: 90px; width: 200px; height: 120px; border-radius: 10px; background: linear-gradient(180deg, #f4f4f6, var(--tube)); }
  .cover__url { position: absolute; bottom: 28px; left: 0; right: 0; text-align: center; font-family: "Comic Neue", "Comic Sans MS", cursive; font-weight: 700; color: var(--paper); font-size: 17px; }
</style>
</head>
<body>
<main class="spread">

  <section class="panel products">
    <h2 class="products__title">Organic Face Cleansers</h2>
    <p class="products__sub">Gentle for All Skin Types</p>

    <article class="product">
      <div class="product__text">
        <h3 class="product__name">Refreshing Natural Cleanser</h3>
        <p class="product__desc">This refreshing aloe-based gel cleanser is formulated with organic ingredients. It cleans thoroughly without drying out the skin. Balances skin hydration and sebum. 4 fl. oz.</p>
      </div>
      <div class="product__shot" role="img" aria-label="Product photo: refreshing cleanser tube"></div>
    </article>

    <article class="product product--shaded">
      <div class="product__text">
        <h3 class="product__name">Hydrating Organic Cleanser</h3>
        <p class="product__desc">This light gel cleanser is formulated with coconut milk and honey for a moisturizing wash. Gently washes away dirt and oil, leaving skin hydrated and softened. 4 fl. oz.</p>
      </div>
      <div class="product__shot" role="img" aria-label="Product photo: hydrating cleanser tube"></div>
    </article>

    <article class="product">
      <div class="product__text">
        <h3 class="product__name">Nourishing Cleansing Milk</h3>
        <p class="product__desc">This comforting organic lotion cleanser is enriched with botanical extracts to leave skin feeling smooth and soft. Can be used to remove eye makeup. 4 fl. oz.</p>
      </div>
      <div class="product__shot" role="img" aria-label="Product photo: cleansing milk tube"></div>
    </article>

    <p class="products__contact">www.corvanyx.com &nbsp;1-855-5-Corvan</p>
  </section>

  <section class="panel back">
    <div class="brand"><span class="brand__dot"></span>Corvanyx</div>
    <div class="soft-band" role="img" aria-label="Soft pink decorative band"></div>
    <div class="back__copy">
      <p class="back__mission">Creating Beauty Solutions<br>through Science</p>
      <div class="back__details">
        <p>www.corvanyx.com</p>
        <p>Customer Service<br>1-855-5-Corvan (855-526-7826)<br>1290 Linden Crest Ave. Suite 400<br>Maple Grove, CA 94580</p>
      </div>
    </div>
  </section>

  <section class="panel cover">
    <div class="brand"><span class="brand__dot"></span>Corvanyx</div>
    <p class="cover__tagline">Bringing You Smart Skin Care</p>
    <div class="cover__portrait" role="img" aria-label="Photo: smiling woman touching her cheek"></div>
    <div class="soft-band" role="img" aria-label="Soft pink decorative band"></div>
    <div class="cover__products" role="img" aria-label="Photo: group of skin care product bottles, tubes and jar"></div>
    <p class="cover__url">www.corvanyx.com</p>
  </section>

</main>
</body>
</html>
```